Redesign the *Settings* screen for the BrelloZ app.

BrelloZ app is in production, but we need to refresh and redesign the settings screen to be cleaner, easier, more intuitive, and more professional looking.

Project Deadline Extended
Reason: Several designers have requested more time. This will also give time to provide feedback on existing designs.

Requirements
Must have
• Black background, so that the screen is consistent with the rest of the app.

```html
<!DOCTYPE html>
<html lang="en">
<head>
<meta charset="utf-8">
<title>BrelloZ Settings</title>
<link rel="stylesheet" href="https://fonts.googleapis.com/css2?family=Ubuntu:wght@300;400&display=swap">
<style>
  :root {
    --page: #373737;
    --status: #000000;
    --bar: #1e1e1e;
    --row: #2e2e2e;
    --divider: #1b1b1b;
    --text: #ffffff;
    --accent: #d0202a;
  }
  * { box-sizing: border-box; margin: 0; padding: 0; }
  html, body { width: 1200px; height: 1130px; overflow: hidden; background: var(--page); }
  body { font-family: "Ubuntu", sans-serif; color: var(--text); position: relative; }
  .screen {
    position: absolute; left: 294px; top: 19px;
    width: 510px; height: 910px;
    transform: scale(1.2); transform-origin: top left;
    background: var(--row); overflow: hidden;
  }
  .status-bar {
    position: absolute; left: 0; top: 0; width: 510px; height: 50px;
    background: var(--status); font-size: 17px; font-weight: 400;
  }
  .status-bar .signal { position: absolute; left: 14px; top: 13px; }
  .status-bar .carrier { position: absolute; left: 116px; top: 12px; }
  .status-bar .wifi { position: absolute; left: 166px; top: 14px; }
  .status-bar .clock { position: absolute; left: 232px; top: 12px; }
  .status-bar .bluetooth { position: absolute; left: 370px; top: 13px; }
  .status-bar .battery-level { position: absolute; left: 390px; top: 12px; }
  .status-bar .battery { position: absolute; left: 434px; top: 13px; }
  .app-bar { position: absolute; left: 0; top: 50px; width: 510px; height: 87px; background: var(--bar); }
  .menu-toggle { position: absolute; left: 30px; top: 30px; }
  .setting-row {
    position: absolute; left: 0; width: 510px; height: 126px;
    background: var(--row); border-bottom: 2px solid var(--divider);
  }
  .setting-label {
    position: absolute; left: 28px; top: 50%; transform: translateY(-50%);
    font-size: 25px; font-weight: 400; letter-spacing: 0.2px; white-space: nowrap;
    display: flex; align-items: center;
  }
  .caret { margin-left: 22px; width: 0; height: 0; border-left: 7px solid transparent; border-right: 7px solid transparent; border-top: 7px solid var(--accent); }
  .help { margin-left: 8px; width: 22px; height: 22px; border: 1.5px solid var(--accent); border-radius: 50%; color: var(--accent); font-size: 15px; font-weight: 300; display: flex; align-items: center; justify-content: center; }
  .option {
    position: absolute; top: 50%; margin-top: -35px; width: 70px; height: 70px; border-radius: 50%;
    border: 3px solid var(--text); display: flex; align-items: center; justify-content: center;
    color: var(--text); font-size: 27px; font-weight: 300;
  }
  .option.is-active { border-color: var(--accent); color: var(--accent); }
  .option-caption { position: absolute; top: 96px; width: 70px; text-align: center; font-size: 17px; font-weight: 300; }
  .firearm-value { position: absolute; right: 20px; top: 50%; transform: translateY(-50%); font-size: 27px; }
  .mode-tags { position: absolute; left: 0; top: 765px; width: 510px; height: 60px; background: var(--row); }
  .tag { position: absolute; top: 12px; width: 48px; height: 38px; font-size: 25px; display: flex; align-items: center; justify-content: center; }
  .tag-train { left: 352px; background: var(--accent); color: var(--text); }
  .tag-train::before { content: ""; position: absolute; top: -7px; left: 17px; border-left: 7px solid transparent; border-right: 7px solid transparent; border-bottom: 7px solid var(--accent); }
  .tag-record { left: 410px; background: var(--text); color: var(--accent); }
  .tag-record::after { content: ""; position: absolute; right: -8px; top: 12px; border-top: 7px solid transparent; border-bottom: 7px solid transparent; border-left: 8px solid var(--text); }
  .tab-bar { position: absolute; left: 0; top: 815px; width: 510px; height: 95px; background: var(--bar); }
  .tab { position: absolute; top: 0; height: 95px; width: 110px; text-align: center; font-size: 16px; font-weight: 300; }
  .tab svg { position: absolute; left: 50%; transform: translateX(-50%); top: 8px; }
  .tab span { position: absolute; left: 0; right: 0; top: 65px; }
  .tab.is-current { color: var(--accent); }
</style>
</head>
<body>
<main class="screen">
  <header class="status-bar">
    <svg class="signal" width="96" height="20" viewBox="0 0 96 20" fill="none" stroke="#fff" stroke-width="1.6">
      <circle cx="8" cy="10" r="7" fill="#fff"/><circle cx="27" cy="10" r="7" fill="#fff"/>
      <circle cx="46" cy="10" r="7"/><circle cx="65" cy="10" r="7"/><circle cx="84" cy="10" r="7"/>
    </svg>
    <span class="carrier">Relay</span>
    <svg class="wifi" width="18" height="16" viewBox="0 0 18 16" fill="none" stroke="#fff" stroke-width="2"><path d="M2 6a10 10 0 0 1 14 0"/><path d="M5 9a6 6 0 0 1 8 0"/><circle cx="9" cy="13" r="1.6" fill="#fff" stroke="none"/></svg>
    <span class="clock">00:01</span>
    <svg class="bluetooth" width="12" height="20" viewBox="0 0 12 20" fill="none" stroke="#fff" stroke-width="1.6"><path d="M2 5l8 9-4 4V2l4 4-8 9"/></svg>
    <span class="battery-level">38%</span>
    <svg class="battery" width="62" height="20" viewBox="0 0 62 20"><rect x="1" y="1" width="54" height="18" rx="2" fill="none" stroke="#fff" stroke-width="2"/><rect x="5" y="5" width="17" height="10" fill="#fff"/><rect x="56" y="6" width="5" height="8" fill="#fff"/></svg>
  </header>

  <nav class="app-bar">
    <svg class="menu-toggle" width="32" height="24" viewBox="0 0 32 24" stroke="#fff" stroke-width="3"><path d="M0 3h32M0 12h32M0 21h32"/></svg>
  </nav>

  <section class="setting-row" style="top:137px">
    <div class="setting-label">Pistol<i class="caret"></i></div>
    <div class="option" style="left:422px">
      <svg width="46" height="38" viewBox="0 0 46 38" fill="none" stroke="#fff" stroke-width="2" stroke-linejoin="round"><path d="M4 6h38v9H22l-2 4h-5l-4 14H4l5-18H4z"/><path d="M15 19l2 6h4"/><path d="M10 10h28"/></svg>
    </div>
  </section>

  <section class="setting-row" style="top:262px">
    <div class="setting-label">Current Firarm<i class="caret"></i></div>
    <div class="firearm-value">KR12</div>
  </section>

  <section class="setting-row" style="top:388px">
    <div class="setting-label">Select Hand</div>
    <div class="option is-active" style="left:335px">
      <svg width="40" height="46" viewBox="0 0 40 46" fill="none" stroke="#d0202a" stroke-width="2.4" stroke-linecap="round" stroke-linejoin="round"><path d="M11 24V8a3 3 0 0 1 6 0v12M17 20V5a3 3 0 0 1 6 0v15M23 20V7a3 3 0 0 1 6 0v15M29 22V12a3 3 0 0 1 6 0v16c0 9-6 15-14 15S8 38 5 31l-3-7a3 3 0 0 1 5-3l4 5"/></svg>
    </div>
    <div class="option-caption" style="left:335px">L</div>
    <div class="option" style="left:420px">
      <svg width="40" height="46" viewBox="0 0 40 46" fill="none" stroke="#fff" stroke-width="2.4" stroke-linecap="round" stroke-linejoin="round"><g transform="translate(40 0) scale(-1 1)"><path d="M11 24V8a3 3 0 0 1 6 0v12M17 20V5a3 3 0 0 1 6 0v15M23 20V7a3 3 0 0 1 6 0v15M29 22V12a3 3 0 0 1 6 0v16c0 9-6 15-14 15S8 38 5 31l-3-7a3 3 0 0 1 5-3l4 5"/></g></svg>
    </div>
    <div class="option-caption" style="left:420px">R</div>
  </section>

  <section class="setting-row" style="top:514px">
    <div class="setting-label">Dry Practice</div>
    <div class="option is-active" style="left:262px">
      <svg width="20" height="48" viewBox="0 0 20 48" fill="none" stroke="#d0202a" stroke-width="2"><path d="M4 18C4 8 10 2 10 2s6 6 6 16v24H4z"/><path d="M3 42h14v4H3zM4 36h12"/></svg>
    </div>
    <div class="option" style="left:342px">
      <svg width="20" height="40" viewBox="0 0 20 40" fill="none" stroke="#fff" stroke-width="2"><rect x="4" y="4" width="12" height="26"/><path d="M2 30h16v6H2z"/></svg>
    </div>
    <div class="option" style="left:422px">CO<sub style="font-size:10px">2</sub></div>
  </section>

  <section class="setting-row" style="top:640px">
    <div class="setting-label">Device Mount Position<i class="help">?</i></div>
    <div class="option is-active" style="left:345px">Fwd</div>
    <div class="option" style="left:422px">Bkd</div>
  </section>

  <div class="mode-tags">
    <div class="tag tag-train">T</div>
    <div class="tag tag-record">R</div>
  </div>

  <footer class="tab-bar">
    <div class="tab" style="left:10px">
      <svg width="52" height="52" viewBox="0 0 52 52" fill="none" stroke="#fff" stroke-width="3"><circle cx="26" cy="26" r="24"/><circle cx="26" cy="26" r="17"/><circle cx="26" cy="26" r="10"/><circle cx="26" cy="26" r="4"/></svg>
      <span>TRAIN</span>
    </div>
    <div class="tab" style="left:134px">
      <svg width="58" height="54" viewBox="0 0 58 54" fill="none" stroke="#fff" stroke-width="3"><rect x="3" y="24" width="12" height="28"/><rect x="23" y="14" width="12" height="38"/><rect x="43" y="2" width="12" height="50"/></svg>
      <span>HISTORY</span>
    </div>
    <div class="tab" style="left:264px">
      <svg width="68" height="40" viewBox="0 0 68 40" fill="none" stroke="#fff" stroke-width="2.4" stroke-linejoin="round" style="top:20px"><path d="M2 12L34 2l32 10-32 10z"/><path d="M14 16v12c8 6 32 6 40 0V16"/><path d="M62 13v14"/></svg>
      <span>LEARN</span>
    </div>
    <div class="tab is-current" style="left:404px">
      <svg width="48" height="48" viewBox="0 0 48 48" fill="none" stroke="#d0202a" stroke-width="2.4" stroke-linejoin="round"><path d="M20 3h8l1 6 5 2 5-4 6 6-4 5 2 5 6 1v8l-6 1-2 5 4 5-6 6-5-4-5 2-1 6h-8l-1-6-5-2-5 4-6-6 4-5-2-5-6-1v-8l6-1 2-5-4-5 6-6 5 4 5-2z"/><circle cx="24" cy="24" r="7"/></svg>
      <span>SETTING</span>
    </div>
  </footer>
</main>
</body>
</html>
```